Real Estate Open House A Frame Sign

The sign is 22" wide and 28" tall. This sign is used to post around the neighbourhood to direct people to an open house (home that is for sale). It is also used for self-promotion.

Designwise
- I just want something with a modern look, simple and clean.
- I want my picture and business logo on the left side.
- On the right side, website (www.lumwick-realestate.com) and my phone (555-374-9126), then a blank space where I can write an address when I need to.

I'm not sure how I want the overall design look. I'm very open-minded and I'm depending on your creative mind to come up with something.

If you have any questions, please let me know.

```html
<!DOCTYPE html>
<html lang="en">
<head>
<meta charset="UTF-8">
<title>Lumwick Real Estate – Open House A-Frame Sign</title>
<link href="https://fonts.googleapis.com/css2?family=Montserrat:wght@300;400;700&display=swap" rel="stylesheet">
<style>
  :root {
    --backdrop: #eef2f3;
    --navy: #13457f;
    --sunflower: #fbbf16;
    --lagoon: #2dbfb1;
    --white: #ffffff;
    --studio-light: #d2d2d2;
    --studio-mid: #a4a4a4;
    --studio-dark: #6f6f6f;
    --suit: #2b313b;
  }
  html, body {
    margin: 0;
    padding: 0;
    width: 1200px;
    height: 640px;
    overflow: hidden;
  }
  body {
    background: radial-gradient(ellipse at center, #fbfcfc 0%, var(--backdrop) 75%);
    font-family: "Montserrat", sans-serif;
    position: relative;
  }
  .sign {
    position: absolute;
    top: 87px;
    width: 362px;
    height: 460px;
    box-shadow: 0 10px 14px -8px rgba(0, 0, 0, 0.28);
  }
  .sign--sunflower { left: 185px; --accent: var(--sunflower); }
  .sign--lagoon { left: 654px; --accent: var(--lagoon); }
  .sign svg { display: block; width: 100%; height: 100%; }
  .sign__field { fill: var(--navy); }
  .sign__swoosh { fill: var(--accent); }
  .sign__address-box { fill: var(--white); }

  .tone-light { stop-color: var(--studio-light); }
  .tone-mid { stop-color: var(--studio-mid); }
  .tone-dark { stop-color: var(--studio-dark); }
  .tone-suit-clear { stop-color: var(--suit); stop-opacity: 0; }
  .tone-suit { stop-color: var(--suit); stop-opacity: 0.85; }

  .brand__name {
    fill: var(--white);
    font-family: "Montserrat", sans-serif;
    font-weight: 300;
    font-size: 27px;
    letter-spacing: 1px;
  }
  .brand__tagline {
    fill: var(--white);
    font-family: "Montserrat", sans-serif;
    font-weight: 400;
    font-size: 9px;
    letter-spacing: 2.6px;
  }
  .contact__phone {
    fill: var(--accent);
    font-family: "Montserrat", sans-serif;
    font-weight: 700;
    font-size: 23px;
    letter-spacing: 1px;
  }
  .contact__web {
    fill: var(--white);
    font-family: "Montserrat", sans-serif;
    font-weight: 700;
    font-size: 13.5px;
    letter-spacing: 0.4px;
  }
</style>
</head>
<body>

  <div class="sign sign--sunflower">
    <svg viewBox="0 0 452 575" xmlns="http://www.w3.org/2000/svg">
      <defs>
        <radialGradient id="studio-a" cx="0.62" cy="0.4" r="0.65">
          <stop offset="0" class="tone-light"/>
          <stop offset="0.55" class="tone-mid"/>
          <stop offset="1" class="tone-dark"/>
        </radialGradient>
        <linearGradient id="suit-a" x1="0" y1="0" x2="0" y2="1">
          <stop offset="0.55" class="tone-suit-clear"/>
          <stop offset="0.85" class="tone-suit"/>
        </linearGradient>
      </defs>
      <rect class="sign__field" width="452" height="575"/>
      <circle class="sign__swoosh" cx="55" cy="207" r="292"/>
      <g role="img" aria-label="Portrait photo of the agent in a dark suit and tie, arms crossed, on a grey studio backdrop">
        <circle cx="80" cy="177" r="252" fill="url(#studio-a)"/>
        <circle cx="80" cy="177" r="252" fill="url(#suit-a)"/>
      </g>
      <text class="brand__name" x="432" y="44" text-anchor="end">LUMWICK</text>
      <text class="brand__tagline" x="432" y="57" text-anchor="end">REAL ESTATE</text>
      <text class="contact__phone" x="426" y="494" text-anchor="end">555-374-9126</text>
      <text class="contact__web" x="426" y="518" text-anchor="end">WWW.LUMWICK-REALESTATE.COM</text>
      <rect class="sign__address-box" x="193" y="527" width="233" height="24"/>
    </svg>
  </div>

  <div class="sign sign--lagoon">
    <svg viewBox="0 0 452 575" xmlns="http://www.w3.org/2000/svg">
      <defs>
        <radialGradient id="studio-b" cx="0.62" cy="0.4" r="0.65">
          <stop offset="0" class="tone-light"/>
          <stop offset="0.55" class="tone-mid"/>
          <stop offset="1" class="tone-dark"/>
        </radialGradient>
        <linearGradient id="suit-b" x1="0" y1="0" x2="0" y2="1">
          <stop offset="0.55" class="tone-suit-clear"/>
          <stop offset="0.85" class="tone-suit"/>
        </linearGradient>
      </defs>
      <rect class="sign__field" width="452" height="575"/>
      <circle class="sign__swoosh" cx="55" cy="207" r="292"/>
      <g role="img" aria-label="Portrait photo of the agent in a dark suit and tie, arms crossed, on a grey studio backdrop">
        <circle cx="80" cy="177" r="252" fill="url(#studio-b)"/>
        <circle cx="80" cy="177" r="252" fill="url(#suit-b)"/>
      </g>
      <text class="brand__name" x="432" y="44" text-anchor="end">LUMWICK</text>
      <text class="brand__tagline" x="432" y="57" text-anchor="end">REAL ESTATE</text>
      <text class="contact__phone" x="426" y="494" text-anchor="end">555-374-9126</text>
      <text class="contact__web" x="426" y="518" text-anchor="end">WWW.LUMWICK-REALESTATE.COM</text>
      <rect class="sign__address-box" x="193" y="527" width="233" height="24"/>
    </svg>
  </div>

</body>
</html>
```